Signage Design Project

We need a logo and signage for the shopfront of a personal fitness training gym and coaching facility. We want the signage to cover the glass shopfront windows which consist of 4 glass windows with dimensions: 1 of 200cm x 180cm, 2 of 180cm x 135cm and 1 of 180cm x 180cm. The windows that are 200x 180 and 180x180 are the most visable/ important. We want the 200x180 to display the logo and our name which is "Harbourline Fitness Centre" with further information of: Your personal training studio and boutique coaching gym Ph: 9472 3815.
For the window with 180 x 180cm measurement we want to list the services we provide which are:
Personal Training Sessions | Group Classes|Weight Loss |Toning & Sculpting|Bodybuilding I Cardio|Weights| Kettlebells| Boxing| Circuits I Team Building Programs| Boot Camp I Healthy Lifestyle & Wellness Coaching
The 2 windows 180x135cm are diagonal to the entry of the shop. We want them to be the same and plainer in design with the words: Harbourline Fitness Centre
Personal Training Studio and Boutique Coaching Gym
The signage design also includes an acrylic window box that lights up which is to display the logo and Harbourline Fitness Centre

```html
<!DOCTYPE html>
<html lang="en">
<head>
<meta charset="utf-8">
<title>Harbourline Fitness Centre – Window Signage</title>
<link href="https://fonts.googleapis.com/css2?family=Arimo:wght@700&family=Roboto+Condensed:wght@700&display=swap" rel="stylesheet">
<style>
  :root {
    --orange: #f6a51c;
    --orange-light: #fbd07a;
    --cream: #fff8ec;
    --blue: #1b9ee0;
    --blue-dark: #0a4f86;
    --ink: #1c1208;
    --silhouette: #3a220c;
    --white: #ffffff;
  }
  html, body {
    margin: 0;
    width: 1200px;
    height: 748px;
    overflow: hidden;
    background: var(--white);
  }
  .canvas {
    position: relative;
    width: 1200px;
    height: 748px;
  }
  .sign {
    position: absolute;
    box-sizing: border-box;
    box-shadow: 4px 5px 8px rgba(0,0,0,0.45);
    font-family: "Arimo", Arial, sans-serif;
    font-weight: 700;
    text-align: center;
  }
  .sign--main {
    left: 46px; top: 66px; width: 425px; height: 360px;
    transform: rotate(-3deg);
    background: linear-gradient(180deg, var(--orange) 0%, var(--orange-light) 55%, var(--cream) 90%);
  }
  .sign--side {
    left: 460px; top: 345px; width: 370px; height: 285px;
    transform: rotate(4deg);
    background: linear-gradient(180deg, var(--orange) 0%, var(--orange-light) 55%, var(--cream) 92%);
  }
  .sign--services {
    left: 818px; top: 50px; width: 375px; height: 375px;
    transform: rotate(-4deg);
    background: var(--orange);
    font-family: "Roboto Condensed", "Arial Narrow", sans-serif;
    text-align: left;
  }
  .brand-name {
    margin: 0;
    color: var(--blue);
    line-height: 1;
    letter-spacing: 0.5px;
  }
  .sign--main .brand-name { padding-top: 16px; font-size: 40px; }
  .sign--side .brand-name { padding-top: 14px; font-size: 33px; }
  .athletes {
    display: block;
    margin: 0 auto;
    background: linear-gradient(180deg, rgba(58,34,12,0) 0%, rgba(58,34,12,0.55) 30%, rgba(58,34,12,0.55) 85%, rgba(58,34,12,0) 100%);
    border-radius: 4px;
  }
  .sign--main .athletes { width: 395px; height: 92px; margin-top: 18px; }
  .sign--side .athletes { width: 340px; height: 80px; margin-top: 14px; }
  .sign--services .athletes { position: absolute; left: 18px; bottom: 16px; width: 340px; height: 74px; }
  .tagline {
    margin: 0;
    color: var(--blue);
    line-height: 1.15;
    text-shadow: 0 0 2px var(--white);
  }
  .sign--main .tagline { margin-top: 14px; font-size: 24px; }
  .sign--side .tagline { margin-top: 14px; font-size: 20px; }
  .phone {
    margin: 14px 0 0;
    color: var(--ink);
    font-size: 37px;
    letter-spacing: 1.5px;
    text-align: left;
    padding-left: 22px;
  }
  .services-head {
    margin: 0;
    padding-top: 16px;
    text-align: center;
    line-height: 1.1;
  }
  .services-head .lead {
    display: block;
    color: var(--blue);
    font-size: 20px;
    text-shadow: 1px 1px 0 var(--blue-dark);
  }
  .services-head .sub {
    display: block;
    color: var(--ink);
    font-size: 20px;
  }
  .service-cols {
    display: flex;
    gap: 16px;
    padding: 40px 12px 0 14px;
  }
  .service-list {
    list-style: none;
    margin: 0;
    padding: 0;
    font-size: 16px;
    line-height: 1.45;
  }
  .service-list li {
    color: var(--white);
    text-shadow: 1px 1px 1px var(--ink), -1px -1px 1px var(--ink);
  }
  .service-list li::before { content: "•"; }
  .service-list li.accent { color: var(--blue); text-shadow: 1px 1px 1px var(--blue-dark); }
  .service-list--left { width: 150px; }
  .service-list--right { width: 180px; }
</style>
</head>
<body>
<div class="canvas">

  <section class="sign sign--main">
    <h1 class="brand-name">Harbourline Fitness Centre</h1>
    <div class="athletes" role="img" aria-label="Row of athlete silhouettes: weightlifter, footballer, cyclist, martial artist, basketball player and baseball batter along a blue line"></div>
    <p class="tagline">Your Personal Training Studio<br>and<br>Boutique Coaching Gym</p>
    <p class="phone">Ph:&nbsp;02 9472 3815</p>
  </section>

  <section class="sign sign--side">
    <h2 class="brand-name">Harbourline Fitness Centre</h2>
    <div class="athletes" role="img" aria-label="Row of athlete silhouettes along a blue line"></div>
    <p class="tagline">Your Personal Training Studio<br>and Boutique Coaching Gym</p>
  </section>

  <section class="sign sign--services">
    <h2 class="services-head">
      <span class="lead">Personal Training Sessions</span>
      <span class="sub">Group Classes</span>
    </h2>
    <div class="service-cols">
      <ul class="service-list service-list--left">
        <li class="accent">Weight Loss</li>
        <li>Toning &amp; Sculpting</li>
        <li class="accent">Bodybuilding</li>
        <li>Cardio</li>
        <li class="accent">Weights</li>
        <li>Kettlebells</li>
        <li class="accent">Boxing</li>
      </ul>
      <ul class="service-list service-list--right">
        <li class="accent">Circuits</li>
        <li>Team Building Programs</li>
        <li class="accent">Boot Camp</li>
        <li>Healthy Lifestyle &amp; Wellness Coaching</li>
      </ul>
    </div>
    <div class="athletes" role="img" aria-label="Row of athlete silhouettes across the bottom of the panel"></div>
  </section>

</div>
</body>
</html>
```